Bright Tin Harbour

I want some thing to stand out

I have a logo that needs to be used

the busines is bassed on a zumbrella page and i need that to bee a key point to go to the page and like it as well

I all so want this to be a card I can have one with just the basic details to have on counters in shops and in clubs

but all so a card with my details on it and other staff when needed

Target Market(s)

Bright Tin harbour is 100% about Whats going on so we Dont sleep we are there for you at sunrise to tell you whats on around you we are with you at lunch to tell you whats good and at tea all so we tell you what clubs are going off and whats hot

Requirements
Must have
• Logo

ZumBrella link/logo
(something to say find us or like us on zumbrella)

NEEDS TO STAND OUT
Should not have
• Details for Card
Manager/Director - Declan Fairweather
M: 0438 555 917
Po Box 3921 Surfers Paradise QLD 4208
E: declan@brighttinharbour-example.com.au
W: brighttinharbour-example.com.au
F: zumbrella-example.com/brighttinharbour#

```html
<!DOCTYPE html>
<html lang="en">
<head>
<meta charset="utf-8">
<title>Bright Tin Harbour – Business Cards</title>
<link href="https://fonts.googleapis.com/css2?family=Josefin+Sans:wght@300;400;600&family=Questrial&display=swap" rel="stylesheet">
<style>
  :root {
    --page-bg: #ffffff;
    --brand-red: #f9264a;
    --card-white: #ffffff;
    --ink-light: #ffffff;
    --ink-grey: #5c5c5c;
    --tagline-grey: #6b6b6b;
    --shadow: rgba(0, 0, 0, 0.16);
  }
  html, body {
    margin: 0;
    padding: 0;
    overflow: hidden;
    background: var(--page-bg);
  }
  .canvas {
    position: relative;
    width: 1200px;
    height: 1000px;
    overflow: hidden;
    background: var(--page-bg);
  }
  .card {
    position: absolute;
    box-shadow: 0 3px 10px var(--shadow);
    box-sizing: border-box;
    overflow: hidden;
  }
  /* Staff details side */
  .card--details {
    left: 155px;
    top: 58px;
    width: 537px;
    height: 537px;
    background: var(--brand-red);
    color: var(--ink-light);
    font-family: "Josefin Sans", "Century Gothic", sans-serif;
    padding: 56px 0 0 48px;
  }
  .staff-name {
    margin: 0;
    font-weight: 600;
    font-size: 35px;
    letter-spacing: 1.2px;
    text-transform: uppercase;
    line-height: 1;
    white-space: nowrap;
  }
  .staff-role {
    margin: 15px 0 0;
    font-weight: 300;
    font-size: 29px;
    letter-spacing: 1px;
    line-height: 1;
  }
  .contact-list {
    list-style: none;
    margin: 47px 0 0;
    padding: 0;
    font-weight: 300;
    line-height: 1;
  }
  .contact-list li { white-space: nowrap; }
  .contact-phone { font-size: 31px; letter-spacing: 1px; }
  .contact-email { font-size: 23px; margin-top: 16px; letter-spacing: 0.5px; }
  .contact-web   { font-size: 23px; margin-top: 15px; letter-spacing: 0.5px; }
  .contact-social {
    font-size: 17px;
    margin-top: 18px;
    letter-spacing: 0.5px;
    text-transform: uppercase;
    font-weight: 300;
  }
  /* Brand side */
  .card--brand {
    left: 507px;
    top: 391px;
    width: 541px;
    height: 541px;
    background: var(--card-white);
    display: flex;
    flex-direction: column;
    align-items: center;
    padding-top: 158px;
  }
  .brand-dot {
    display: block;
    width: 100px;
    height: 100px;
  }
  .brand-name {
    margin: 54px 0 0;
    font-family: "Questrial", "Century Gothic", sans-serif;
    font-weight: 400;
    font-size: 56px;
    color: var(--ink-grey);
    line-height: 1;
    white-space: nowrap;
  }
  .brand-tagline {
    margin: 22px 0 0;
    font-family: "Josefin Sans", "Century Gothic", sans-serif;
    font-weight: 300;
    font-size: 17px;
    letter-spacing: 1.4px;
    color: var(--tagline-grey);
    text-transform: uppercase;
    white-space: nowrap;
  }
</style>
</head>
<body>
<main class="canvas">
  <section class="card card--details" aria-label="Staff business card">
    <h1 class="staff-name">Declan Fairweather</h1>
    <p class="staff-role">Manager/Director</p>
    <ul class="contact-list">
      <li class="contact-phone">0438 555 917</li>
      <li class="contact-email">declan@brighttinharbour-example.net</li>
      <li class="contact-web">brighttinharbour-example.net</li>
      <li class="contact-social">zumbrella-example.com/brighttinharbour#</li>
    </ul>
  </section>

  <section class="card card--brand" aria-label="Brand business card">
    <svg class="brand-dot" viewBox="0 0 100 100" aria-hidden="true">
      <circle cx="50" cy="50" r="50" fill="var(--brand-red)"/>
    </svg>
    <h2 class="brand-name">Bright Tin Harbour</h2>
    <p class="brand-tagline">What's happening all around the harbour?</p>
  </section>
</main>
</body>
</html>
```